Business card for Northland's Blue Wagon.

Good day i am looking for a business card design for my business.
The name of the business is Northland's Blue Wagon. It is a van rental business that provides a driver and helper to the customer. Customer have use to van for small moves, studio or 1 bedroom, Moving furniture like couch or kitchen cabinets.
We are available evenings, weekends and holidays.
the means to contact us is by phone at 628-947-2071; By emails at Oakridge@northlandsbluewagon.net; or by social media, Facebook and Instagram.
You can see attached pictures of the van and or logo.

```html
<!DOCTYPE html>
<html lang="en">
<head>
<meta charset="utf-8">
<title>Northland's Blue Wagon – Business Card</title>
<link rel="stylesheet" href="https://fonts.googleapis.com/css2?family=Montserrat:wght@400;500;600;700&display=swap">
<style>
  :root {
    --card-red: #c42b21;
    --card-red-deep: #a9221a;
    --ink: #000000;
    --paper: #ffffff;
    --stage: #111111;
    --accent-icon: #d8332a;
  }
  * { box-sizing: border-box; margin: 0; padding: 0; }
  html, body {
    width: 1200px;
    height: 1145px;
    overflow: hidden;
    background: var(--stage);
    font-family: "Montserrat", sans-serif;
  }
  .sheet {
    position: relative;
    width: 1200px;
    height: 1145px;
  }
  .card {
    position: absolute;
    left: 135px;
    width: 930px;
    height: 530px;
    background: var(--card-red);
    overflow: hidden;
  }
  .card--front { top: 22px; }
  .card--back { top: 592px; }

  /* Front side */
  .logo-band {
    position: absolute;
    left: 650px;
    top: 152px;
    width: 280px;
    height: 226px;
    background: var(--paper);
    border-radius: 113px 0 0 113px;
  }
  .brand-mark {
    position: absolute;
    left: 700px;
    top: 152px;
    width: 230px;
    height: 226px;
    display: flex;
    flex-direction: column;
    align-items: center;
    justify-content: center;
    gap: 12px;
  }
  .brand-mark__dot {
    width: 70px;
    height: 70px;
    border-radius: 50%;
    background: var(--card-red);
  }
  .brand-mark__name {
    font-weight: 600;
    font-size: 15px;
    color: var(--ink);
    text-align: center;
    line-height: 1.25;
  }
  .contact-panel {
    position: absolute;
    left: 0;
    top: 125px;
    width: 678px;
    height: 280px;
    background: var(--ink);
    border-radius: 0 140px 140px 0;
    padding: 63px 0 0 60px;
    color: var(--paper);
  }
  .company-name {
    font-weight: 600;
    font-size: 38px;
    letter-spacing: 0.3px;
    line-height: 1;
    margin-bottom: 28px;
  }
  .contact-list { list-style: none; }
  .contact-list li {
    display: flex;
    align-items: center;
    gap: 14px;
    font-size: 19px;
    font-weight: 400;
    height: 30px;
  }
  .contact-list svg { width: 18px; height: 18px; flex: none; }

  /* Back side */
  .promo-band {
    position: absolute;
    left: 40px;
    top: 120px;
    width: 890px;
    height: 280px;
    background: var(--paper);
    border-radius: 140px 0 0 140px;
  }
  .van-photo {
    position: absolute;
    left: 60px;
    top: 148px;
    width: 430px;
    height: 262px;
    border-radius: 40px 60px 30px 90px;
    background: linear-gradient(160deg, #d8261f 0%, #b01a16 55%, #3b3b3b 100%);
  }
  .taglines {
    position: absolute;
    right: 38px;
    top: 190px;
    text-align: right;
    font-weight: 700;
    font-size: 29px;
    line-height: 55px;
    color: var(--ink);
  }
  .tag-bar {
    position: absolute;
    right: 0;
    top: 203px;
    width: 22px;
    height: 127px;
    background: var(--ink);
  }
</style>
</head>
<body>
<main class="sheet">

  <section class="card card--front" aria-label="Business card front">
    <div class="logo-band"></div>
    <div class="brand-mark">
      <span class="brand-mark__dot"></span>
      <span class="brand-mark__name">Northland's Blue Wagon</span>
    </div>
    <div class="contact-panel">
      <h1 class="company-name">Northland's Blue Wagon</h1>
      <ul class="contact-list">
        <li>
          <svg viewBox="0 0 24 24" aria-hidden="true"><path fill="var(--accent-icon)" d="M6.6 10.8a15.1 15.1 0 0 0 6.6 6.6l2.2-2.2c.3-.3.7-.4 1-.2 1.1.4 2.3.6 3.6.6.6 0 1 .4 1 1V20c0 .6-.4 1-1 1A17 17 0 0 1 3 4c0-.6.4-1 1-1h3.5c.6 0 1 .4 1 1 0 1.3.2 2.5.6 3.6.1.3 0 .7-.2 1z"/></svg>
          +1 (628)-947-2071
        </li>
        <li>
          <svg viewBox="0 0 24 24" aria-hidden="true"><circle cx="12" cy="12" r="4" fill="none" stroke="var(--accent-icon)" stroke-width="2.4"/><path d="M16 8v5a3 3 0 0 0 6 0v-1a10 10 0 1 0-4 8" fill="none" stroke="var(--accent-icon)" stroke-width="2.4"/></svg>
          Oakridge@northlandsbluewagon.net
        </li>
        <li>
          <svg viewBox="0 0 24 24" aria-hidden="true"><g fill="none" stroke="var(--accent-icon)" stroke-width="2"><circle cx="12" cy="12" r="9.5"/><ellipse cx="12" cy="12" rx="4" ry="9.5"/><path d="M2.5 12h19M4 7h16M4 17h16"/></g></svg>
          www.northlandsbluewagon.net
        </li>
      </ul>
    </div>
  </section>

  <section class="card card--back" aria-label="Business card back">
    <div class="promo-band"></div>
    <div class="van-photo" role="img" aria-label="Photo of the company's red cargo van with driver service livery"></div>
    <p class="taglines">
      Your friend with the van<br>
      Van rental with driver<br>
      Evenings and weekeands
    </p>
    <div class="tag-bar"></div>
  </section>

</main>
</body>
</html>
```